Infografik/ Zeitleiste für Startup
Zielgruppe
Wir sind ein Startup, das über die Seite Zeitwabe.de zukünftig folgenden Service anbietet: Unternehmer können sehr flexibel (selbst) gestaltete Terminformulare erstellen und auf Ihrer Website einbinden. Kunden können dann diese Termine buchen und bekommen dann Erinnerungs-Mails und SMS.
Zielgruppe: Dienstleister wie Fotografen, Friseure, Versicherungsvertreter, Masseure, Restaurants, Arztpraxen. Also alle, die darauf angewiesen sind, dass vereinbarte Termine eingehalten werden und die die Terminvereinbarung vereinfachen wollen. Also weniger per Telefon, mehr über die eigene Website.
Zeitwabe ist mit LobPunkt.com (aktuell noch Top-und-Flop.com) verknüpft. Kunden, die einen Termin wünschen, sehen die Bewertungen vorheriger Kunden. Das stärkt das Vertrauen und erhöht die Termin-Zuverlässigkeit (Verbessert die No-Show-Rate). Damit sinken auch die Werbekosten je Kunden (geringere Kosten pro Conversion).
Zeitwabe.de und LobPunkt.com (aktuell noch Top-und-Flop.com) wurde vom Team von Bild-Kontor.de entwickelt. Dank Zeitwabe und LobPunkt.com haben wir (das Team von Bild-Kontor.de) folgende Vorteile:
- verbesserte Termin-Zuverlässigkeit (No-Show-Rate)
- mehr Kunden, mehr Shootings
- höherer Umsatz
- Zeitersparnis bei der Terminvereinbarung
- Senkungen der Werbekosten je Kunden (geringere Kosten pro Conversion)
Das ist der Grund, warum wir Zeitwabe und LobPunkt nun auch für andere Branchen anbieten.
Siehe auch: https://www.videoportal-beispiel.de/watch?v=qRtmZZk_31p
Siehe auch: https://www.videoportal-beispiel.de/watch?v=wLpoNNe_74x
Aufgabenstellung
Wir benötigen für Zeitwabe.de eine Infografik. Diese soll verdeutlichen, welche Vorteile wir (Bild-Kontor.de) dank Zeitwabe und LobPunkt haben:
Der Betrachter soll diese Zahlen auf einen Blick werten und die Vorteile für SEIN GESCHÄFT erkennen können. Zum Beispiel anhand einer Zeitleiste, die die Entwicklung der verschiedenen Kennzahlen wiedergibt.
Die Kennzahlen (die Entwicklung) können Sie hier aufrufen: https://ablage-beispiel.de/ordner/7KrtWmPq2ZxN8-vbYy3HsLd0QaTeRcU?teilen=ja
Besonders soll die positive Entwicklung ab Ende September 2017 deutlich werden. Ab Ende September 2017 haben wir Zeitwabe und LobPunkt.com für die Terminvereinbarung genutzt. Vorher haben wir Termine per Email und Telefon vereinbart, was deutlich zeitintensiver war.
Das Design der Zeitleiste (der Infografik) soll sich an Zeitwabe.de orientieren.
Falls die sechs Kennzahlen nicht übersichtlich in einer Zeitleiste darstellbar sind, könnten die Kennzahlen auf mehrere Grafiken aufgeteilt werden.
Vorstellbar ist auch eine interaktive Infografik, bei der man die jeweilige Kennzahl auswählen kann.
Wir lassen uns hier gerne von Ihrer Kreativität überraschen. Der spätere Kunde/Nutzer/ Betrachter der Infografik steht bitte im Vordergrund jeder Überlegung/jedes Designs.
Nutzen Sie ggf. bitte Icons und verschiedenen Farben, um die verschiedenen Kennzahlen auch visuell zu verdeutlichen.
Die Infografik soll später auf https://entwickler.zeitwabe.de/de/ueber-uns.html und in Flyern veröffentlicht werden.
Wesentliche Funktionen und Vorteile siehe auch:
https://www.videoportal-beispiel.de/watch?v=qRtmZZk_31p
https://www.videoportal-beispiel.de/watch?v=wLpoNNe_74x
Die einzelnen gr..

```html
<!DOCTYPE html>
<html lang="de">
<head>
<meta charset="utf-8">
<title>Zeitwabe – Kennzahlen-Zeitleiste</title>
<link rel="stylesheet" href="https://fonts.googleapis.com/css2?family=Barlow:wght@400&family=Barlow+Semi+Condensed:wght@600;700&display=swap">
<style>
  :root{
    --red:#e30613; --green:#8bb827; --yellow:#ffcc00;
    --panel:#767c7f; --panel-light:#a3a8aa; --shade:#e9eaeb;
    --strip:#f1f2f2; --tick:#c9cccd; --value:#6f7375; --white:#fff;
  }
  *{margin:0;padding:0;box-sizing:border-box}
  html,body{width:1200px;height:726px;overflow:hidden;background:var(--white)}
  .infographic{position:relative;width:1200px;height:726px;font-family:"Barlow",sans-serif}
  .metric{position:absolute;left:0;width:1200px}
  .metric svg{position:absolute;left:0;top:0;display:block}
  .metric-label{position:absolute;left:0;top:0;width:118px;height:23px;padding-left:10px;
    font:700 13px/23px "Barlow Semi Condensed",sans-serif;letter-spacing:.6px;color:var(--white)}
  .is-red .metric-label{background:var(--red)}
  .is-green .metric-label{background:var(--green)}
  .is-yellow .metric-label{background:var(--yellow)}
  .value{font:400 10.5px "Barlow",sans-serif;fill:var(--value);text-anchor:middle}
  .trend{font:700 22px "Barlow Semi Condensed",sans-serif;fill:var(--white);letter-spacing:1px}
  .arrow{fill:none;stroke:var(--white);stroke-width:2.5;stroke-linejoin:miter}
  .timeline{position:absolute;left:0;top:664px;width:1200px;height:28px}
  .month{font:400 7.5px "Barlow",sans-serif;fill:var(--value);text-anchor:middle}
  .phase{position:absolute;top:692px;height:34px;color:var(--white);text-align:center;
    font:700 14.5px/34px "Barlow Semi Condensed",sans-serif;letter-spacing:1.2px}
  .phase-before{left:0;width:427px;background:var(--panel-light)}
  .phase-after{left:434px;width:766px;background:var(--panel)}
</style>
</head>
<body>
<div class="infographic">

  <!-- SHOOTINGS -->
  <section class="metric is-red" style="top:0;height:112px">
    <svg width="1200" height="112" viewBox="0 0 1200 112">
      <rect x="118" y="7" width="314" height="105" fill="var(--shade)"/>
      <rect x="1077" y="7" width="123" height="105" fill="var(--panel)"/>
      <rect x="0" y="0" width="1200" height="7" fill="var(--red)"/>
      <circle cx="57.5" cy="66.5" r="30" fill="var(--red)" role="img" aria-label="Symbol Kamerablende"/>
      <g stroke="var(--tick)" stroke-width="0.8"><path d="M160 7v15M215 7v15M268.5 7v15M323 7v15M378 7v15M431.5 7v15M486.5 7v15M541.5 7v15M596 7v15M650.5 7v15M705.5 7v15M760 7v15M814.5 7v15M869 7v15M923.5 7v15M978 7v15M1032.5 7v15"/></g>
      <g fill="var(--red)" transform="translate(0 85) scale(1 -2.72)">
        <rect x="156" width="8" height="9"/><rect x="211" width="8" height="8"/><rect x="264.5" width="8" height="10"/><rect x="319" width="8" height="9"/><rect x="374" width="8" height="10"/><rect x="427.5" width="8" height="12"/><rect x="482.5" width="8" height="13"/><rect x="537.5" width="8" height="9"/><rect x="592" width="8" height="16"/><rect x="646.5" width="8" height="19"/><rect x="701.5" width="8" height="23"/><rect x="756" width="8" height="21"/><rect x="810.5" width="8" height="18"/><rect x="865" width="8" height="20"/><rect x="919.5" width="8" height="15"/><rect x="974" width="8" height="12"/><rect x="1028.5" width="8" height="25"/>
      </g>
      <g class="values">
        <text class="value" x="160" y="98">9</text><text class="value" x="215" y="98">8</text><text class="value" x="268.5" y="98">10</text><text class="value" x="323" y="98">9</text><text class="value" x="378" y="98">10</text><text class="value" x="431.5" y="98">12</text><text class="value" x="486.5" y="98">13</text><text class="value" x="541.5" y="98">9</text><text class="value" x="596" y="98">16</text><text class="value" x="650.5" y="98">19</text><text class="value" x="705.5" y="98">23</text><text class="value" x="760" y="98">21</text><text class="value" x="814.5" y="98">18</text><text class="value" x="869" y="98">20</text><text class="value" x="923.5" y="98">15</text><text class="value" x="978" y="98">12</text><text class="value" x="1032.5" y="98">25</text>
      </g>
      <text class="trend" x="1085" y="71">+ XX %</text>
      <path class="arrow" d="M1077 86H1152L1175 45M1165 48L1175 45L1177 56"/>
    </svg>
    <div class="metric-label">SHOOTINGS</div>
  </section>

  <!-- KUNDEN -->
  <section class="metric is-green" style="top:112px;height:109px">
    <svg width="1200" height="109" viewBox="0 0 1200 109">
      <rect x="118" y="6" width="314" height="103" fill="var(--shade)"/>
      <rect x="1077" y="6" width="123" height="103" fill="var(--panel)"/>
      <rect x="0" y="0" width="1200" height="6" fill="var(--green)"/>
      <circle cx="57.5" cy="64.5" r="30" fill="var(--green)" role="img" aria-label="Figur eines zufriedenen Kunden"/>
      <g stroke="var(--tick)" stroke-width="0.8"><path d="M160 6v15M215 6v15M268.5 6v15M323 6v15M378 6v15M431.5 6v15M486.5 6v15M541.5 6v15M596 6v15M650.5 6v15M705.5 6v15M760 6v15M814.5 6v15M869 6v15M923.5 6v15M978 6v15M1032.5 6v15"/></g>
      <g fill="var(--green)" transform="translate(0 81) scale(1 -0.158)">
        <rect x="156" width="8" height="144"/><rect x="211" width="8" height="128"/><rect x="264.5" width="8" height="160"/><rect x="319" width="8" height="145"/><rect x="374" width="8" height="161"/><rect x="427.5" width="8" height="216"/><rect x="482.5" width="8" height="221"/><rect x="537.5" width="8" height="153"/><rect x="592" width="8" height="272"/><rect x="646.5" width="8" height="323"/><rect x="701.5" width="8" height="391"/><rect x="756" width="8" height="357"/><rect x="810.5" width="8" height="306"/><rect x="865" width="8" height="340"/><rect x="919.5" width="8" height="355"/><rect x="974" width="8" height="204"/><rect x="1028.5" width="8" height="425"/>
      </g>
      <g>
        <text class="value" x="160" y="94">144</text><text class="value" x="215" y="94">128</text><text class="value" x="268.5" y="94">160</text><text class="value" x="323" y="94">145</text><text class="value" x="378" y="94">161</text><text class="value" x="431.5" y="94">216</text><text class="value" x="486.5" y="94">221</text><text class="value" x="541.5" y="94">153</text><text class="value" x="596" y="94">272</text><text class="value" x="650.5" y="94">323</text><text class="value" x="705.5" y="94">391</text><text class="value" x="760" y="94">357</text><text class="value" x="814.5" y="94">306</text><text class="value" x="869" y="94">340</text><text class="value" x="923.5" y="94">355</text><text class="value" x="978" y="94">204</text><text class="value" x="1032.5" y="94">425</text>
      </g>
      <text class="trend" x="1085" y="66">+ XX %</text>
      <path class="arrow" d="M1077 81H1152L1185 18M1175 21L1185 18L1186 29"/>
    </svg>
    <div class="metric-label">KUNDEN</div>
  </section>

  <!-- UMSATZ -->
  <section class="metric is-yellow" style="top:221px;height:111px">
    <svg width="1200" height="111" viewBox="0 0 1200 111">
      <rect x="118" y="7" width="314" height="104" fill="var(--shade)"/>
      <rect x="1077" y="7" width="123" height="104" fill="var(--panel)"/>
      <rect x="0" y="0" width="1200" height="7" fill="var(--yellow)"/>
      <circle cx="57.5" cy="65.5" r="30" fill="var(--yellow)" role="img" aria-label="Symbol Euro-Münze"/>
      <g stroke="var(--tick)" stroke-width="0.8"><path d="M160 7v15M215 7v15M268.5 7v15M323 7v15M378 7v15M431.5 7v15M486.5 7v15M541.5 7v15M596 7v15M650.5 7v15M705.5 7v15M760 7v15M814.5 7v15M869 7v15M923.5 7v15M978 7v15M1032.5 7v15"/></g>
      <g fill="var(--yellow)" transform="translate(0 79) scale(1 -0.333)">
        <rect x="156" width="8" height="100"/><rect x="211" width="8" height="97"/><rect x="264.5" width="8" height="97"/><rect x="319" width="8" height="94"/><rect x="374" width="8" height="97"/><rect x="427.5" width="8" height="102"/><rect x="482.5" width="8" height="105"/><rect x="537.5" width="8" height="102"/><rect x="592" width="8" height="108"/><rect x="646.5" width="8" height="114"/><rect x="701.5" width="8" height="131"/><rect x="756" width="8" height="128"/><rect x="810.5" width="8" height="142"/><rect x="865" width="8" height="137"/><rect x="919.5" width="8" height="157"/><rect x="974" width="8" height="154"/><rect x="1028.5" width="8" height="174"/>
      </g>
      <g>
        <text class="value" x="158" y="94">100</text><text class="value" x="158" y="105">(Basis)</text><text class="value" x="212" y="94">97</text><text class="value" x="268.5" y="94">97</text><text class="value" x="324.5" y="94">94</text><text class="value" x="377" y="94">97</text><text class="value" x="431.5" y="94">102</text><text class="value" x="487.5" y="94">105</text><text class="value" x="542" y="94">102</text><text class="value" x="596.5" y="94">108</text><text class="value" x="651" y="94">114</text><text class="value" x="705" y="94">131</text><text class="value" x="760" y="94">128</text><text class="value" x="814.5" y="94">142</text><text class="value" x="869" y="94">137</text><text class="value" x="923.5" y="94">157</text><text class="value" x="978" y="94">154</text><text class="value" x="1032.5" y="94">174</text>
      </g>
      <text class="trend" x="1085" y="62">+ 74 %</text>
      <path class="arrow" d="M1077 78H1152L1172 41M1162 44L1172 41L1174 52"/>
    </svg>
    <div class="metric-label">UMSATZ</div>
  </section>

  <!-- NO-SHOW-RATE -->
  <section class="metric is-red" style="top:332px;height:112px">
    <svg width="1200" height="112" viewBox="0 0 1200 112">
      <rect x="118" y="7" width="314" height="105" fill="var(--shade)"/>
      <rect x="1077" y="7" width="123" height="105" fill="var(--panel)"/>
      <rect x="0" y="0" width="1200" height="7" fill="var(--red)"/>
      <circle cx="57.5" cy="67" r="30" fill="var(--red)" role="img" aria-label="Symbol leerer Sessel"/>
      <g stroke="var(--tick)" stroke-width="0.8"><path d="M160 7v15M215 7v15M268.5 7v15M323 7v15M378 7v15M431.5 7v15M486.5 7v15M541.5 7v15M596 7v15M650.5 7v15M705.5 7v15M760 7v15M814.5 7v15M869 7v15M923.5 7v15M978 7v15M1032.5 7v15"/></g>
      <g fill="var(--red)" transform="translate(0 88) scale(1 -1.77)">
        <rect x="156" width="8" height="30"/><rect x="211" width="8" height="28"/><rect x="264.5" width="8" height="31"/><rect x="319" width="8" height="27"/><rect x="374" width="8" height="29"/><rect x="427.5" width="8" height="15"/><rect x="482.5" width="8" height="14"/><rect x="537.5" width="8" height="13"/><rect x="592" width="8" height="15"/><rect x="646.5" width="8" height="13"/><rect x="701.5" width="8" height="12"/><rect x="756" width="8" height="13"/><rect x="810.5" width="8" height="12"/><rect x="865" width="8" height="11"/><rect x="919.5" width="8" height="12"/><rect x="974" width="8" height="13"/><rect x="1028.5" width="8" height="12"/>
      </g>
      <g>
        <text class="value" x="159" y="102">30</text><text class="value" x="215" y="102">28</text><text class="value" x="267" y="102">31</text><text class="value" x="324.5" y="102">27</text><text class="value" x="378" y="102">29</text><text class="value" x="432" y="102">15</text><text class="value" x="487.5" y="102">14</text><text class="value" x="542" y="102">13</text><text class="value" x="596.5" y="102">15</text><text class="value" x="650.5" y="102">13</text><text class="value" x="705.5" y="102">12</text><text class="value" x="760" y="102">13</text><text class="value" x="814.5" y="102">12</text><text class="value" x="869" y="102">11</text><text class="value" x="923.5" y="102">12</text><text class="value" x="978" y="102">13</text><text class="value" x="1032.5" y="102">12</text>
      </g>
      <text class="trend" x="1085" y="46">- XX %</text>
      <path class="arrow" d="M1077 61.5H1152L1170 92M1169 81L1170 92L1160 88"/>
    </svg>
    <div class="metric-label">NO-SHOW-RATE</div>
  </section>

  <!-- ZEITAUFWAND -->
  <section class="metric is-green" style="top:444px;height:110px">
    <svg width="1200" height="110" viewBox="0 0 1200 110">
      <rect x="118" y="7" width="314" height="103" fill="var(--shade)"/>
      <rect x="1077" y="7" width="123" height="103" fill="var(--panel)"/>
      <rect x="0" y="0" width="1200" height="7" fill="var(--green)"/>
      <circle cx="57.5" cy="68" r="30" fill="var(--green)" role="img" aria-label="Symbol Stoppuhr"/>
      <g stroke="var(--tick)" stroke-width="0.8"><path d="M160 7v15M215 7v15M268.5 7v15M323 7v15M378 7v15M431.5 7v15M486.5 7v15M541.5 7v15M596 7v15M650.5 7v15M705.5 7v15M760 7v15M814.5 7v15M869 7v15M923.5 7v15M978 7v15M1032.5 7v15"/></g>
      <g fill="var(--green)" transform="translate(0 82) scale(1 -0.786)">
        <rect x="156" width="8" height="61"/><rect x="211" width="8" height="60"/><rect x="264.5" width="8" height="63"/><rect x="319" width="8" height="61"/><rect x="374" width="8" height="63"/><rect x="427.5" width="8" height="12"/><rect x="482.5" width="8" height="10"/><rect x="537.5" width="8" height="11"/><rect x="592" width="8" height="12"/><rect x="646.5" width="8" height="11"/><rect x="701.5" width="8" height="12"/><rect x="756" width="8" height="11"/><rect x="810.5" width="8" height="12"/><rect x="865" width="8" height="10"/><rect x="919.5" width="8" height="9"/><rect x="974" width="8" height="10"/><rect x="1028.5" width="8" height="13"/>
      </g>
      <g>
        <text class="value" x="159" y="98">61</text><text class="value" x="215" y="98">60</text><text class="value" x="269.5" y="98">63</text><text class="value" x="324.5" y="98">61</text><text class="value" x="379" y="98">63</text><text class="value" x="432" y="98">12</text><text class="value" x="487" y="98">10</text><text class="value" x="541.5" y="98">11</text><text class="value" x="596.5" y="98">12</text><text class="value" x="650.5" y="98">11</text><text class="value" x="705.5" y="98">12</text><text class="value" x="760" y="98">11</text><text class="value" x="814.5" y="98">12</text><text class="value" x="869" y="98">10</text><text class="value" x="923.5" y="98">9</text><text class="value" x="978" y="98">10</text><text class="value" x="1032.5" y="98">13</text>
      </g>
      <text class="trend" x="1085" y="40">- XX %</text>
      <path class="arrow" d="M1077 54.5H1152L1176 101M1175 90L1176 101L1166 96"/>
    </svg>
    <div class="metric-label">ZEITAUFWAND</div>
  </section>

  <!-- WERBEKOSTEN -->
  <section class="metric is-yellow" style="top:554px;height:110px">
    <svg width="1200" height="110" viewBox="0 0 1200 110">
      <rect x="118" y="7" width="314" height="103" fill="var(--shade)"/>
      <rect x="1077" y="7" width="123" height="103" fill="var(--panel)"/>
      <rect x="0" y="0" width="1200" height="7" fill="var(--yellow)"/>
      <circle cx="57.5" cy="66.5" r="30" fill="var(--yellow)" role="img" aria-label="Symbol Megafon"/>
      <g stroke="var(--tick)" stroke-width="0.8"><path d="M160 7v15M215 7v15M268.5 7v15M323 7v15M378 7v15M431.5 7v15M486.5 7v15M541.5 7v15M596 7v15M650.5 7v15M705.5 7v15M760 7v15M814.5 7v15M869 7v15M923.5 7v15M978 7v15M1032.5 7v15"/></g>
      <g fill="var(--yellow)" transform="translate(0 76) scale(1 -0.39)">
        <rect x="156" width="8" height="100"/><rect x="211" width="8" height="96"/><rect x="264.5" width="8" height="103"/><rect x="319" width="8" height="100"/><rect x="374" width="8" height="100"/><rect x="427.5" width="8" height="80"/><rect x="482.5" width="8" height="70"/><rect x="537.5" width="8" height="67"/><rect x="592" width="8" height="67"/><rect x="646.5" width="8" height="63"/><rect x="701.5" width="8" height="63"/><rect x="756" width="8" height="67"/><rect x="810.5" width="8" height="70"/><rect x="865" width="8" height="67"/><rect x="919.5" width="8" height="60"/><rect x="974" width="8" height="63"/><rect x="1028.5" width="8" height="67"/>
      </g>
      <g>
        <text class="value" x="158" y="92">100</text><text class="value" x="158" y="103">(Basis)</text><text class="value" x="215" y="92">96</text><text class="value" x="266" y="92">103</text><text class="value" x="323" y="92">100</text><text class="value" x="377" y="92">100</text><text class="value" x="432" y="92">80</text><text class="value" x="487" y="92">70</text><text class="value" x="541.5" y="92">67</text><text class="value" x="596" y="92">67</text><text class="value" x="650.5" y="92">63</text><text class="value" x="705.5" y="92">63</text><text class="value" x="760" y="92">67</text><text class="value" x="814.5" y="92">70</text><text class="value" x="869" y="92">67</text><text class="value" x="923.5" y="92">60</text><text class="value" x="978" y="92">63</text><text class="value" x="1032.5" y="92">67</text>
      </g>
      <text class="trend" x="1085" y="58">- 33 %</text>
      <path class="arrow" d="M1077 72H1152L1170 105M1169 94L1170 105L1160 100"/>
    </svg>
    <div class="metric-label">WERBEKOSTEN</div>
  </section>

  <!-- Zeitachse -->
  <svg class="timeline" width="1200" height="28" viewBox="0 0 1200 28">
    <rect x="0" y="0" width="1077" height="28" fill="var(--strip)"/>
    <rect x="1077" y="0" width="123" height="28" fill="var(--panel)"/>
    <g stroke="var(--tick)" stroke-width="0.8"><path d="M160 0v12M215 0v12M268.5 0v12M323 0v12M378 0v12M431.5 0v12M486.5 0v12M541.5 0v12M596 0v12M650.5 0v12M705.5 0v12M760 0v12M814.5 0v12M869 0v12M923.5 0v12M978 0v12M1032.5 0v12"/></g>
    <text class="month" x="160" y="24">Mai 17</text><text class="month" x="215" y="24">Juni 17</text><text class="month" x="268.5" y="24">Juli 17</text><text class="month" x="323" y="24">Aug 17</text><text class="month" x="378" y="24">Sep 17</text><text class="month" x="430" y="24">Okt 17</text><text class="month" x="486.5" y="24">Nov17</text><text class="month" x="541.5" y="24">Dez 17</text><text class="month" x="596" y="24">Jan 18</text><text class="month" x="650.5" y="24">Feb 18</text><text class="month" x="705.5" y="24">Mär 18</text><text class="month" x="760" y="24">Apr 18</text><text class="month" x="814.5" y="24">Mai 18</text><text class="month" x="869" y="24">Jun 18</text><text class="month" x="923.5" y="24">Jul 18</text><text class="month" x="978" y="24">Aug 18</text><text class="month" x="1032.5" y="24">Sep 18</text>
  </svg>

  <div class="phase phase-before">OHNE TERMIN-TOOL</div>
  <div class="phase phase-after">NUTZUNG ZEITWABE UND LOBPUNKT</div>
</div>
</body>
</html>
```